Business Card Design - Local Discount Club

Looking for a fun business card for a local discount club. One side should be the logo only and the other should be have :

Name
Title
Phone, Email
Website

```html
<!DOCTYPE html>
<html lang="en">
<head>
<meta charset="utf-8">
<title>Harbor Perks Club – Business Card</title>
<link href="https://fonts.googleapis.com/css2?family=Montserrat:wght@400;500;700&display=swap" rel="stylesheet">
<style>
  :root {
    --navy: #1d3a8a;
    --royal: #2e52b0;
    --sky: #5bc0eb;
    --lime: #7cb342;
    --ink: #2b2b2b;
    --paper: #ffffff;
    --stage: #e9eaec;
  }
  * { box-sizing: border-box; margin: 0; padding: 0; }
  html, body {
    width: 1200px; height: 786px; overflow: hidden;
    background: var(--stage);
    font-family: "Montserrat", sans-serif;
  }
  .sheet { position: relative; width: 1200px; height: 786px; }

  .card {
    position: absolute; top: 238px;
    width: 540px; height: 310px;
    box-shadow: 0 6px 18px rgba(0,0,0,.18);
    overflow: hidden;
  }
  .card--front { left: 45px; background: var(--paper); }
  .card--back  { left: 615px; background: var(--navy); }

  /* front */
  .brand {
    position: absolute; left: 34px; top: 118px;
    width: 210px;
    display: flex; align-items: center; gap: 10px;
  }
  .brand__dot {
    flex: none; width: 14px; height: 14px; border-radius: 50%;
    background: var(--sky);
  }
  .brand__name {
    font-weight: 700; font-size: 26px; line-height: 1.05;
    color: var(--royal); letter-spacing: .5px;
  }
  .divider {
    position: absolute; left: 272px; top: 70px;
    width: 1.5px; height: 150px; background: var(--royal);
  }
  .contact { position: absolute; left: 300px; top: 72px; color: var(--ink); }
  .contact__name { font-weight: 700; font-size: 19px; color: var(--royal); }
  .contact__title { font-size: 12px; margin-top: 1px; }
  .contact__list { list-style: none; margin-top: 12px; font-size: 11.5px; line-height: 17px; }
  .contact__list li { display: flex; align-items: center; gap: 9px; }
  .contact__list svg { width: 11px; height: 11px; fill: var(--royal); flex: none; }
  .contact__address { margin-top: 14px; font-size: 11.5px; line-height: 15px; padding-left: 20px; }

  .stripes { position: absolute; left: 0; bottom: 0; width: 540px; height: 44px; }

  /* back */
  .back-brand {
    position: absolute; inset: 0;
    display: flex; align-items: center; justify-content: center; gap: 14px;
  }
  .back-brand__dot { width: 18px; height: 18px; border-radius: 50%; background: var(--sky); }
  .back-brand__name {
    font-weight: 700; font-size: 36px; line-height: 1.05;
    color: var(--paper); letter-spacing: .5px;
  }
</style>
</head>
<body>
<main class="sheet">

  <section class="card card--front" aria-label="Business card front">
    <div class="brand">
      <span class="brand__dot"></span>
      <span class="brand__name">Harbor Perks Club</span>
    </div>

    <div class="divider"></div>

    <div class="contact">
      <p class="contact__name">Lena Marsh</p>
      <p class="contact__title">Owner</p>
      <ul class="contact__list">
        <li>
          <svg viewBox="0 0 24 24" aria-hidden="true"><path d="M6.6 10.8a15.1 15.1 0 0 0 6.6 6.6l2.2-2.2c.3-.3.7-.4 1-.2 1.1.4 2.3.6 3.6.6.6 0 1 .4 1 1V20c0 .6-.4 1-1 1A17 17 0 0 1 3 4c0-.6.4-1 1-1h3.5c.6 0 1 .4 1 1 0 1.3.2 2.5.6 3.6.1.3 0 .7-.2 1z"/></svg>
          +49 400 555 0123
        </li>
        <li>
          <svg viewBox="0 0 24 24" aria-hidden="true"><path d="M2 5h20v14H2zm2 2v.5l8 5 8-5V7l-8 5z"/></svg>
          hello@harborperks.com
        </li>
        <li>
          <svg viewBox="0 0 24 24" aria-hidden="true"><circle cx="12" cy="12" r="10"/></svg>
          www.harborperks.com
        </li>
      </ul>
      <p class="contact__address">Lindenweg 42<br>20095 Hamburg</p>
    </div>

    <svg class="stripes" viewBox="0 0 540 44" preserveAspectRatio="none" aria-hidden="true">
      <polygon points="0,34 262,34 256,44 0,44" fill="var(--navy)"/>
      <polygon points="270,24 440,24 430,44 258,44" fill="var(--sky)"/>
      <polygon points="448,14 540,14 540,44 436,44" fill="var(--lime)"/>
    </svg>
  </section>

  <section class="card card--back" aria-label="Business card back">
    <div class="back-brand">
      <span class="back-brand__dot"></span>
      <span class="back-brand__name">Harbor Perks Club</span>
    </div>
  </section>

</main>
</body>
</html>
```